Metallic gold accent business card design using new logo

We need a new business card design utilizing our new logo and emphasizing a clean, sophisticated, elegant, easy to read card. Would like to use metallic gold accent, especially with the new logo design, but not overused. Thinking Black with metallic gold printing on reverse side. Front side off white in colour with logo or emblem, and basic information/writing. Logo and emblem should not be too large, would like the overall theme to be classic, even perhaps a bit understated.

Target Market(s)

High end custom home clientele. Sophisticated and elegant

Industry/Entity Type

Residential Construction

Contact Information for Business Card

Looking to use an online provider like ZIB or similar for printing the cards, if you need design details for applying the gold foil, it has to be set up as an element.

Font styles to use
Serif

Colors
fefbee

Requirements
Must have
• My information:
• Warren Pelt
• Owner
• war@hollowbeambuilders.ca
• (555) 317-4609 or (555) 726-4609
• www.hollowbeambuilders.ca
Should not have
• Colourful designs full of images or large logos, large text, flashy gold everywhere

```html
<!DOCTYPE html>
<html lang="en">
<head>
<meta charset="utf-8">
<title>Hollow Beam Builders — Business Card</title>
<link rel="stylesheet" href="https://fonts.googleapis.com/css2?family=Cinzel:wght@600&family=Open+Sans:wght@400&display=swap">
<style>
  :root {
    --backdrop: #e9e6df;
    --card-front: #fefbee;
    --card-back: #2c2b29;
    --gold: #b8912f;
    --gold-light: #d4b15a;
    --ink: #1c1c1c;
  }
  * { box-sizing: border-box; margin: 0; padding: 0; }
  html, body { width: 1200px; height: 1000px; overflow: hidden; }
  body { background: var(--backdrop); position: relative; font-family: "Open Sans", Arial, sans-serif; }

  .card {
    position: absolute;
    left: 266px;
    width: 666px;
    height: 397px;
    box-shadow: 0 3px 10px rgba(0,0,0,0.25);
  }
  .card--front { top: 74px; background: var(--card-front); }
  .card--back { top: 534px; background: var(--card-back); }

  .brand {
    position: absolute;
    font-family: "Cinzel", Georgia, serif;
    font-weight: 600;
    text-align: center;
    line-height: 1.15;
  }
  .card--front .brand {
    left: 30px; width: 272px; top: 222px;
    color: var(--gold);
    font-size: 24px;
    letter-spacing: 2px;
  }
  .card--back .brand {
    left: 0; width: 666px; top: 258px;
    color: var(--gold-light);
    font-size: 34px;
    letter-spacing: 4px;
  }

  .divider {
    position: absolute;
    left: 320px; top: 109px;
    width: 1.5px; height: 177px;
    background: var(--gold);
  }

  .contact-block { position: absolute; left: 354px; top: 108px; }
  .contact-name {
    font-family: "Cinzel", Georgia, serif;
    font-weight: 600;
    font-size: 20px;
    letter-spacing: 0.5px;
    color: var(--gold);
    line-height: 24px;
  }
  .contact-role { font-size: 16px; color: var(--ink); line-height: 22px; }

  .contact-list { list-style: none; margin-top: 38px; }
  .contact-list li {
    display: flex; align-items: center;
    font-size: 16px; color: var(--ink);
    height: 24.5px;
  }
  .contact-icon { width: 14px; height: 12px; margin-right: 6px; fill: var(--gold); flex: none; }
</style>
</head>
<body>

  <section class="card card--front" aria-label="Card front">
    <div class="brand">Hollow Beam<br>Builders</div>
    <div class="divider"></div>
    <div class="contact-block">
      <div class="contact-name">WARREN PELT</div>
      <div class="contact-role">Owner</div>
      <ul class="contact-list">
        <li>
          <svg class="contact-icon" viewBox="0 0 14 12" aria-hidden="true"><path d="M1 4c0-2 3-3 6-3s6 1 6 3v1h-3V3.5H4V5H1z"/><path d="M3 6h8l1 5H2z"/></svg>
          (555) 726-4609
        </li>
        <li>
          <svg class="contact-icon" viewBox="0 0 14 12" aria-hidden="true"><path d="M1 4c0-2 3-3 6-3s6 1 6 3v1h-3V3.5H4V5H1z"/><path d="M3 6h8l1 5H2z"/></svg>
          (555) 317-4609
        </li>
        <li>
          <svg class="contact-icon" viewBox="0 0 14 12" aria-hidden="true"><path d="M1 2h12v8H1z"/><path d="M1.5 2.5L7 7l5.5-4.5" fill="none" stroke="#fefbee" stroke-width="1"/></svg>
          war@hollowbeambuilders.ca
        </li>
        <li>
          <svg class="contact-icon" viewBox="0 0 14 12" aria-hidden="true"><circle cx="7" cy="6" r="5.5"/><path d="M1.5 6h11M7 0.5v11M3.5 2.5q3.5 2 7 0M3.5 9.5q3.5-2 7 0" fill="none" stroke="#fefbee" stroke-width="0.8"/></svg>
          www.hollowbeambuilders.ca
        </li>
      </ul>
    </div>
  </section>

  <section class="card card--back" aria-label="Card back">
    <div class="brand">Hollow Beam<br>Builders</div>
  </section>

</body>
</html>
```